Quillory Nest Business Card

I need a business card design. We are a collaborate online training company. Our colors are gray and green. Our website is QuilloryNest.com

I would like an area for a profile picture within the card

```html
<!DOCTYPE html>
<html lang="en">
<head>
<meta charset="utf-8">
<title>Quillory Nest Business Card</title>
<link rel="stylesheet" href="https://fonts.googleapis.com/css2?family=Open+Sans:wght@300;400;700&display=swap">
<style>
  :root {
    --backdrop: #e9e7e2;
    --card: #f8f9fa;
    --card-white: #ffffff;
    --ink: #1d1d1b;
    --ink-soft: #3a3a3a;
    --green: #7dc242;
    --green-deep: #5fa52c;
    --portrait-bg: #eef0f1;
    --portrait-fill: #3c3c3c;
  }
  * { box-sizing: border-box; margin: 0; padding: 0; }
  html, body {
    width: 1200px;
    height: 1023px;
    overflow: hidden;
    background: var(--backdrop);
    font-family: "Open Sans", Arial, sans-serif;
  }
  .card {
    position: absolute;
    left: 300px;
    width: 600px;
    height: 343px;
    background: var(--card);
    box-shadow: 0 6px 18px rgba(0,0,0,0.18);
    overflow: hidden;
  }
  .card--front { top: 110px; }
  .card--back { top: 570px; background: var(--card-white); }

  /* Front */
  .brand {
    position: absolute;
    left: 120px;
    top: 140px;
    display: flex;
    align-items: center;
    gap: 18px;
  }
  .brand__dot {
    width: 56px;
    height: 56px;
    border-radius: 50%;
    background: var(--green);
  }
  .brand__name {
    font-weight: 700;
    font-size: 52px;
    letter-spacing: -1.5px;
    color: var(--ink);
    line-height: 1;
  }

  /* Back */
  .contact {
    position: absolute;
    left: 44px;
    top: 58px;
    color: var(--ink);
  }
  .contact__name {
    font-weight: 400;
    font-size: 26px;
    line-height: 1.1;
  }
  .contact__role {
    font-weight: 300;
    font-size: 17px;
    color: var(--ink-soft);
    margin-bottom: 34px;
  }
  .contact__line {
    font-weight: 300;
    font-size: 16px;
    line-height: 1.55;
    color: var(--ink-soft);
  }
  .portrait-frame {
    position: absolute;
    right: 0;
    top: 0;
    width: 300px;
    height: 329px;
  }
  .accent-band {
    position: absolute;
    left: 0;
    bottom: 0;
    width: 100%;
    height: 14px;
    background: var(--green);
    border-top: 2px solid var(--green-deep);
  }
</style>
</head>
<body>
  <section class="card card--front">
    <div class="brand">
      <span class="brand__dot"></span>
      <span class="brand__name">Quillory Nest</span>
    </div>
  </section>

  <section class="card card--back">
    <div class="contact">
      <p class="contact__name">Jonah Pell</p>
      <p class="contact__role">Director</p>
      <p class="contact__line">0123 456 789</p>
      <p class="contact__line">jonah@quillorynest.com</p>
      <p class="contact__line">www.QuilloryNest.com</p>
    </div>

    <svg class="portrait-frame" viewBox="0 0 300 329" aria-hidden="false">
      <polygon points="70,0 300,0 300,329 0,329" fill="var(--portrait-bg)"/>
      <line x1="210" y1="22" x2="250" y2="0" stroke="var(--green)" stroke-width="9"/>
      <rect x="80" y="70" width="170" height="259" rx="0" fill="var(--portrait-fill)" opacity="0.85"
            role="img" aria-label="Profile picture of the cardholder"/>
    </svg>

    <div class="accent-band"></div>
  </section>
</body>
</html>
```